Discreet simple classy for adult entertainment

I would like a matte black business card with gold writing for my business. Keeping it simple. Having my following:

Lana frost
Events. Entertainment. Promotions
0491726580

or alternatively could have what i had on my previous card below but i think i prefer the above as again - discretion.

Maybe a nice gold line thru the card or some other very simple design . Or not open to ideas/ can be doublesided if any good ideas with that.

included pics of my old bus card. not sure weather i want a photo on it or not. if i do it wont be the same pic. i kinda wanted a card that was discreet so if it was in someones wallet they wouldn't neccessarily realise it was from a stripper.

Target Market(s)

men

Industry/Entity Type

Business

Contact Information for Business Card

Lana frost
0491726580

Requirements
Nice to have
• i don't know i am really open to anything. im giving my cards to guys so something they can have in their wallet that is discreet preferably.

```html
<!DOCTYPE html>
<html lang="en">
<head>
<meta charset="UTF-8">
<title>Lana Frost — Business Card</title>
<link rel="stylesheet" href="https://fonts.googleapis.com/css2?family=Marcellus+SC&family=Alegreya+Sans:wght@400&display=swap">
<style>
  :root {
    --page: #ffffff;
    --card: #231f20;
    --gold-light: #e2c383;
    --gold-mid: #c59a52;
    --gold-deep: #8e6a2e;
  }
  html, body {
    margin: 0;
    padding: 0;
    width: 1200px;
    height: 960px;
    overflow: hidden;
    background: var(--page);
  }
  .canvas {
    position: relative;
    width: 1200px;
    height: 960px;
  }
  .card {
    position: absolute;
    left: 70px;
    top: 174px;
    width: 1060px;
    height: 606px;
    background: var(--card);
  }
  .gold-text {
    background: linear-gradient(180deg, var(--gold-light) 0%, var(--gold-mid) 50%, var(--gold-deep) 100%);
    -webkit-background-clip: text;
    background-clip: text;
    color: transparent;
  }
  .card__name {
    position: absolute;
    left: 0;
    right: 0;
    top: 120px;
    margin: 0;
    text-align: center;
    font-family: "Marcellus SC", serif;
    font-weight: 400;
    font-size: 150px;
    line-height: 1;
    letter-spacing: 4px;
  }
  .card__services {
    position: absolute;
    left: 0;
    right: 0;
    top: 302px;
    margin: 0;
    text-align: center;
    font-family: "Alegreya Sans", sans-serif;
    font-size: 45px;
    line-height: 1.2;
    color: var(--gold-mid);
    letter-spacing: 0.5px;
  }
  .card__services .dot {
    display: inline-block;
    margin: 0 10px;
  }
  .card__contact {
    position: absolute;
    left: 66px;
    right: 66px;
    top: 392px;
    height: 64px;
    display: flex;
    align-items: center;
    gap: 8px;
  }
  .card__rule {
    flex: 1;
    height: 3px;
    background: linear-gradient(90deg, var(--gold-deep), var(--gold-mid), var(--gold-deep));
  }
  .card__phone {
    font-family: "Alegreya Sans", sans-serif;
    font-size: 56px;
    line-height: 1;
    color: var(--gold-mid);
    letter-spacing: 1px;
  }
</style>
</head>
<body>
  <main class="canvas">
    <section class="card" aria-label="Business card">
      <h1 class="card__name gold-text">Lana Frost</h1>
      <p class="card__services">Events<span class="dot">·</span>Entertainment<span class="dot">·</span>Promotions</p>
      <div class="card__contact">
        <span class="card__rule"></span>
        <span class="card__phone">0491726580</span>
        <span class="card__rule"></span>
      </div>
    </section>
  </main>
</body>
</html>
```